Web Site for Strategy and Technology Consulting Company

We are looking for a website design that engages potential customers to understand our services and contact us. In this contest, we are looking for a homepage design, but the winning designer will be favored for the design of some of the more complicated interior pages of the site. An additional contest (or contests) for these pages will be added soon.

PLATROM AND RESPONSIVE DESIGN
The site will be implemented in WordPress using the Elementor page builder.
We are looking for a design that will look good on phones are well as laptop browsers.

UPLOADED FILES INCLUDE:
1a A wireframe of the homepage we are looking for. The Uploaded PDF also includes a draft of the text proposed for the homepage. Designers are free to go beyond the wireframe, but all elements of the wireframe should be included.
1b A Word document with the draft text of the homepage.
2a-d The Norvalith logo. Two versions are included – a dark version which works well against a light background, and a light version which works well against a dark background.
3 The Norvalith color palette with HEX and RGB values. Designers are not limited to this palette, but colors should be complementary.
4 A draft of the homepage menu
5 Service sheets with information on the services we provide

MORE ABOUT NORVALITH
Norvalith is a consulting company focused on transforming businesses through software. Our tagline, “Transformation Delivered,” recognizes the gap business often have between business transformation and the software they end up with. By listening to our customers and understanding their vision and where they are, we help get our customers where they want to go.

We increase our capability by working with many consultants and partners, allowing us to provide our customers with the best people and the software that best suits them.

Industry/Entity Type

Consulting

Number of Pages Required

1 page

Font styles to use
Sans Serif

Requirements
Must have
• the content represented on the wireframe uploaded
Nice to have
• interactive features, such as roll-over icons that reveal additional information

```html
<!DOCTYPE html>
<html lang="en">
<head>
<meta charset="utf-8">
<title>Norvalith – Transformation Delivered</title>
<link href="https://fonts.googleapis.com/css2?family=Roboto:wght@300;400;500;700&display=swap" rel="stylesheet">
<style>
:root{
  --blue:#2862a6;
  --blue-dark:#1d4f8c;
  --yellow:#e3b60c;
  --sky:#bddcf1;
  --pale:#edf4fb;
  --lavender:#98a8f2;
  --ink:#1f2b3a;
  --text:#3b4250;
  --grey-bg:#e9edf1;
  --footer:#232b37;
  --white:#ffffff;
}
*{box-sizing:border-box;margin:0;padding:0}
html,body{width:1200px;height:3906px;overflow:hidden}
body{font-family:"Roboto",Arial,sans-serif;color:var(--text);background:var(--white);position:relative}
.section{position:absolute;left:0;width:1200px;overflow:hidden}
.abs{position:absolute}
.btn{position:absolute;display:flex;align-items:center;justify-content:center;background:var(--yellow);color:var(--ink);font-weight:500;font-size:13px;letter-spacing:.3px;text-transform:uppercase}
.btn.blue{background:var(--blue);color:var(--white)}
h2{font-weight:300;color:var(--ink);font-size:37px}

/* hero */
.hero{top:0;height:539px;background:linear-gradient(180deg,#2c63a9 0%,#3d6aa8 22%,#7483ab 42%,#a58fa3 52%,#4b5a78 64%,#2f3546 100%)}
.brand{font-weight:400;font-size:36px;color:var(--white);letter-spacing:.2px}
.nav{position:absolute;top:52px;font-size:13px;color:var(--white)}
.nav.active{color:var(--yellow)}
.caret{font-size:9px;margin-left:4px}
.hero-title{position:absolute;top:132px;left:0;width:1200px;text-align:center;font-size:50px;font-weight:400;color:var(--white)}
.hero-title span{color:var(--yellow)}
.hero-sub{position:absolute;top:199px;width:1200px;text-align:center;font-size:13.5px;color:var(--white)}

/* partner strip */
.partners{top:539px;height:159px;background:var(--pale)}
.partner{position:absolute;top:48px;width:144px;height:62px;background:var(--white);box-shadow:0 2px 8px rgba(30,60,110,.12);display:flex;align-items:center;justify-content:center;font-size:19px;font-weight:500;color:#2c3440}

/* about */
.about{top:698px;height:629px;background:var(--white)}
.visual{position:absolute;left:38px;top:53px;width:584px;height:516px;border-radius:50%;background:radial-gradient(circle,#d9dde3 0%,#eef1f4 55%,#ffffff 72%)}
.stat{position:absolute;display:flex;flex-direction:column;align-items:center;justify-content:center;color:var(--white);text-align:center;box-shadow:0 4px 12px rgba(0,0,0,.18)}
.stat b{font-weight:500;line-height:1}
.stat small{font-size:9px;margin-top:4px}
.sq{position:absolute}
.about h2{position:absolute;left:670px;top:122px;font-size:37px}
.para{font-size:12.5px;line-height:19px;color:var(--text)}
.bullets{list-style:none}
.bullets li{position:relative;padding-left:19px;font-size:12.5px;line-height:19px}
.bullets li:before{content:"";position:absolute;left:0;top:5px;width:9px;height:9px;background:var(--yellow)}

/* services */
.services{top:1327px;height:481px;background:var(--sky)}
.services h2{position:absolute;top:52px;width:1200px;text-align:center}
.services .para{position:absolute;top:116px;left:265px;width:670px;text-align:center}
.card{position:absolute;top:208px;width:179px;height:210px;background:var(--white);display:flex;flex-direction:column;align-items:center;text-align:center;padding-top:26px;box-shadow:0 2px 6px rgba(0,0,0,.06)}
.card svg{width:64px;height:64px}
.card h3{font-size:17px;font-weight:500;color:var(--ink);margin-top:14px;line-height:21px}
.card .arrow{margin-top:10px;color:var(--yellow);font-size:20px}
.card.featured{background:var(--blue)}
.card.featured h3{color:var(--white)}
.card.featured p{color:var(--white);font-size:11px;line-height:15px;margin-top:8px;padding:0 22px}

/* resources */
.resources{top:1808px;height:554px;background:var(--white)}
.resources h2{position:absolute;left:121px;top:124px}
.resources .para,.resources .bullets li{font-size:12px;line-height:18.5px}
.resource-photo{position:absolute;left:684px;top:129px;width:393px;height:363px;background:linear-gradient(135deg,#0e2036 0%,#27476d 45%,#7996b4 70%,#1a2f4b 100%)}

/* testimonials */
.testimonials{top:2362px;height:576px;background:var(--grey-bg)}
.testimonials h2{position:absolute;top:55px;width:1200px;text-align:center}
.t-card{position:absolute;top:135px;width:305px;height:375px;background:var(--white);box-shadow:0 3px 10px rgba(0,0,0,.06)}
.t-top{position:absolute;left:0;top:0;width:305px;height:232px;background:var(--blue);padding:36px 22px 0}
.t-top p{color:var(--white);font-size:11.5px;line-height:21px;margin-top:18px}
.avatar{position:absolute;left:114px;top:192px;width:77px;height:77px;border-radius:50%;background:linear-gradient(180deg,#c8ccd2,#8a939e);border:3px solid var(--white)}
.t-name{position:absolute;top:290px;width:305px;text-align:center;font-size:16px;font-weight:500;color:var(--ink)}
.stars{position:absolute;top:320px;width:305px;text-align:center;color:var(--yellow);font-size:17px;letter-spacing:5px}
.chev{position:absolute;top:305px}

/* cta */
.cta{top:2938px;height:240px;background:var(--yellow)}
.cta h2{position:absolute;top:50px;width:1200px;text-align:center;color:var(--white);font-weight:400;font-size:38px}
.cta p{position:absolute;top:107px;width:1200px;text-align:center;color:var(--white);font-size:14px}

/* contact */
.contact{top:3178px;height:485px;background:#f1f1f1}
.map{position:absolute;left:121px;top:65px;width:471px;height:352px;background:linear-gradient(135deg,#e4e6e9,#d3d7dc)}
.contact h2{position:absolute;left:702px;top:58px}
.field{position:absolute;left:702px;width:372px;height:40px;border:1.5px solid #8a8f96;background:var(--white);font-size:12.5px;color:var(--text);padding:12px 18px}

/* footer */
.footer{top:3663px;height:243px;background:var(--footer);color:var(--white)}
.footer h4{position:absolute;top:46px;font-weight:400;font-size:19px}
.footer .small{position:absolute;font-size:9.5px;line-height:15px}
.divider{position:absolute;top:49px;width:1px;height:103px;background:#6b7482}
.social{position:absolute;top:186px;width:22px;height:18px;background:#e7ecf2;border-radius:2px}
</style>
</head>
<body>

<!-- Hero -->
<section class="section hero" role="img" aria-label="Photo of a city skyline with stadium at dusk along a river">
  <div class="abs brand" style="left:121px;top:36px">Norvalith</div>
  <span class="nav active" style="left:347px">Home</span>
  <span class="nav" style="left:438px">About Us<span class="caret">▼</span></span>
  <span class="nav" style="left:545px">Services<span class="caret">▼</span></span>
  <span class="nav" style="left:648px">Insights<span class="caret">▼</span></span>
  <span class="nav" style="left:743px">Join Us<span class="caret">▼</span></span>
  <span class="nav" style="left:840px">Contact Us</span>
  <div class="btn" style="left:962px;top:41px;width:115px;height:36px;font-size:12px">Contact Us</div>
  <h1 class="hero-title">Transformation <span>Delivered</span></h1>
  <p class="hero-sub">Norvalith is a consulting company focused on transforming businesses through software.</p>
  <div class="btn" style="left:537px;top:238px;width:126px;height:40px">Get Started</div>
</section>

<!-- Partners -->
<section class="section partners">
  <div class="partner" style="left:124px">Qivra</div>
  <div class="partner" style="left:287px">Metrion</div>
  <div class="partner" style="left:449px">Orabyte</div>
  <div class="partner" style="left:610px">Staffly</div>
  <div class="partner" style="left:771px">Plotwise</div>
  <div class="partner" style="left:931px">Frostbase</div>
</section>

<!-- About -->
<section class="section about">
  <div class="visual" role="img" aria-label="Illustration of city towers with a dotted halo"></div>
  <div class="sq" style="left:440px;top:182px;width:38px;height:38px;background:var(--lavender)"></div>
  <div class="sq" style="left:482px;top:223px;width:23px;height:23px;background:var(--yellow)"></div>
  <div class="sq" style="left:322px;top:303px;width:24px;height:24px;background:var(--blue)"></div>
  <div class="stat" style="left:146px;top:250px;width:133px;height:79px;background:var(--lavender)"><b style="font-size:42px">43</b><small>Verified client reviews</small></div>
  <div class="stat" style="left:353px;top:250px;width:69px;height:56px;background:var(--yellow)"><b style="font-size:15px">70%</b><small>client return rate</small></div>
  <div class="stat" style="left:440px;top:252px;width:146px;height:95px;background:var(--blue)"><b style="font-size:46px">189</b><small style="font-size:10px">Millions $ raised by clients</small></div>
  <div class="stat" style="left:121px;top:347px;width:64px;height:56px;background:var(--yellow)"><b style="font-size:15px">70%</b><small>repeat work</small></div>
  <div class="stat" style="left:196px;top:365px;width:89px;height:67px;background:#c4dcf6;color:var(--blue)"><b style="font-size:18px;font-weight:400">70%</b><small>client return rate</small></div>
  <div class="stat" style="left:305px;top:352px;width:109px;height:74px;background:#2a2b2e"><b style="font-size:22px">200K</b><small>contributed hours</small></div>

  <h2>Transformation Delivered.</h2>
  <p class="para abs" style="left:670px;top:180px;width:410px">We do more for our customers than implement software. We listen. We work to understand where they are in their transformation journey and where they want to go. We partner with them to clear the roadblocks that stand in their way, ensuring they reach their destination. At Norvalith, we:</p>
  <ul class="bullets abs" style="left:670px;top:281px;width:410px">
    <li style="margin-bottom:8px">Focus on business value, with an emphasis on delivering value quickly.</li>
    <li style="margin-bottom:8px">Meet our customers where they are without backing them up to the beginning of their journey.</li>
    <li style="margin-bottom:8px">Provide a wide range of services, from strategy to product support.</li>
    <li>Commit to our customer’s long-term success.</li>
  </ul>
  <div class="btn" style="left:670px;top:449px;width:116px;height:38px">Our Story</div>
</section>

<!-- Services -->
<section class="section services">
  <h2>Transformation Supported by Technology</h2>
  <p class="para">During our early years, Norvalith focused only on business transformation. We came to realize that successful transformation often depended on quality software implementations, and often more than one. Now we focus on five things, the five things most businesses need to reach their goals.</p>

  <div class="card" style="left:121px">
    <svg viewBox="0 0 64 64"><rect x="6" y="40" width="8" height="18" fill="#2862a6"/><rect x="18" y="32" width="8" height="26" fill="#2862a6"/><rect x="30" y="26" width="8" height="32" fill="#2862a6"/><rect x="42" y="16" width="8" height="42" fill="#2862a6"/><rect x="54" y="8" width="6" height="50" fill="#2862a6"/><path d="M4 34 L22 20 L34 24 L56 6" stroke="#6fa8e6" stroke-width="3" fill="none"/></svg>
    <h3>Business<br>Transformation</h3><div class="arrow">→</div>
  </div>
  <div class="card" style="left:316px">
    <svg viewBox="0 0 64 64"><circle cx="32" cy="38" r="18" fill="none" stroke="#1d4f8c" stroke-width="9" stroke-dasharray="7 4"/><circle cx="32" cy="38" r="9" fill="#2862a6"/><circle cx="18" cy="10" r="5" fill="#4d86cf"/><circle cx="32" cy="8" r="5" fill="#2862a6"/><circle cx="46" cy="10" r="5" fill="#4d86cf"/></svg>
    <h3>ERP<br>Implementations</h3><div class="arrow">→</div>
  </div>
  <div class="card featured" style="left:508px">
    <svg viewBox="0 0 64 64"><circle cx="32" cy="28" r="18" fill="none" stroke="#e3b60c" stroke-width="7" stroke-dasharray="6 4"/><path d="M8 42 L22 34 L32 40 L42 34 L56 42 L40 56 L24 56 Z" fill="#e3b60c"/></svg>
    <h3>CRM<br>Implementations</h3><p>Take your relationships to the next level.</p>
  </div>
  <div class="card" style="left:702px">
    <svg viewBox="0 0 64 64"><ellipse cx="26" cy="12" rx="16" ry="6" fill="#2862a6"/><rect x="10" y="16" width="32" height="12" rx="3" fill="#1d4f8c"/><rect x="10" y="31" width="32" height="12" rx="3" fill="#2862a6"/><rect x="10" y="46" width="32" height="12" rx="3" fill="#1d4f8c"/><path d="M46 22 H56 V10 M46 52 H56 V40" stroke="#6fa8e6" stroke-width="2" fill="none"/><circle cx="58" cy="8" r="3" fill="#6fa8e6"/><circle cx="58" cy="38" r="3" fill="#6fa8e6"/></svg>
    <h3>BI<br>and Data</h3><div class="arrow">→</div>
  </div>
  <div class="card" style="left:897px">
    <svg viewBox="0 0 64 64"><circle cx="32" cy="16" r="9" fill="#2862a6"/><circle cx="14" cy="26" r="7" fill="#4d86cf"/><circle cx="50" cy="26" r="7" fill="#4d86cf"/><rect x="2" y="36" width="22" height="20" rx="8" fill="#4d86cf"/><rect x="40" y="36" width="22" height="20" rx="8" fill="#4d86cf"/><rect x="18" y="28" width="28" height="28" rx="10" fill="#1d4f8c"/></svg>
    <h3>Building the Right<br>Team of People</h3><div class="arrow">→</div>
  </div>
</section>

<!-- Resources -->
<section class="section resources">
  <h2>Resources</h2>
  <p class="para abs" style="left:124px;top:185px;width:420px">The world has changed in the past twenty years. The people you need might not all work for one company. Our clients want the best resources, available quickly. That’s why, in addition to our team of experts, we partner with:</p>
  <ul class="bullets abs" style="left:121px;top:256px;width:420px">
    <li style="margin-bottom:19px">A large network of expert consultants who are the best at what they do,</li>
    <li>Service providers all over the world to provide the resources and value that are right for you, available 24 x 7. People are invariably at the center of our customer’s success. Find out how we can add our experts to yours.</li>
  </ul>
  <div class="btn" style="left:121px;top:382px;width:116px;height:40px">Our Team</div>

  <div class="resource-photo" role="img" aria-label="Photo of a businessman touching a glowing upward arrow above rising arrows"></div>
  <div class="sq" style="left:583px;top:73px;width:47px;height:53px;background:var(--yellow)"></div>
  <div class="sq" style="left:731px;top:62px;width:35px;height:35px;background:var(--lavender)"></div>
  <div class="sq" style="left:595px;top:137px;width:35px;height:35px;background:#c4dcf6"></div>
  <div class="sq" style="left:640px;top:111px;width:88px;height:91px;background:var(--blue)"></div>
  <div class="sq" style="left:734px;top:152px;width:35px;height:35px;background:var(--yellow)"></div>
</section>

<!-- Testimonials -->
<section class="section testimonials">
  <h2>Client Testimonials</h2>
  <svg class="chev" style="left:96px" width="14" height="26" viewBox="0 0 14 26"><path d="M12 2 L2 13 L12 24" stroke="#2862a6" stroke-width="2" fill="none"/></svg>
  <svg class="chev" style="left:1088px" width="14" height="26" viewBox="0 0 14 26"><path d="M2 2 L12 13 L2 24" stroke="#2862a6" stroke-width="2" fill="none"/></svg>

  <div class="t-card" style="left:121px">
    <div class="t-top">
      <svg width="34" height="26" viewBox="0 0 34 26"><path d="M2 2 H14 V12 L8 24 H4 L8 12 H2 Z M19 2 H31 V12 L25 24 H21 L25 12 H19 Z" fill="none" stroke="#fff" stroke-width="2"/></svg>
      <p>For the last 25+ years, the professionals at Brightlane Systems have seamlessly provided all of our computer wants and needs. From supplying hardware and internet connectivity, to support of our sometimes quirky veterinary software...</p>
    </div>
    <div class="avatar" role="img" aria-label="Client portrait"></div>
    <div class="t-name">L.K. Dornvale, D.V.M., M.S.</div>
    <div class="stars">★★★★★</div>
  </div>
  <div class="t-card" style="left:446px">
    <div class="t-top">
      <svg width="34" height="26" viewBox="0 0 34 26"><path d="M2 2 H14 V12 L8 24 H4 L8 12 H2 Z M19 2 H31 V12 L25 24 H21 L25 12 H19 Z" fill="none" stroke="#fff" stroke-width="2"/></svg>
      <p>For the last 25+ years, the professionals at Brightlane Systems have seamlessly provided all of our computer wants and needs. From supplying hardware and internet connectivity, to support of our sometimes quirky veterinary software...</p>
    </div>
    <div class="avatar" role="img" aria-label="Client portrait"></div>
    <div class="t-name">Owen Talbrook</div>
    <div class="stars">★★★★★</div>
  </div>
  <div class="t-card" style="left:771px">
    <div class="t-top">
      <svg width="34" height="26" viewBox="0 0 34 26"><path d="M2 2 H14 V12 L8 24 H4 L8 12 H2 Z M19 2 H31 V12 L25 24 H21 L25 12 H19 Z" fill="none" stroke="#fff" stroke-width="2"/></svg>
      <p>For the last 25+ years, the professionals at Brightlane Systems have seamlessly provided all of our computer wants and needs. From supplying hardware and internet connectivity, to support of our sometimes quirky veterinary software...</p>
    </div>
    <div class="avatar" role="img" aria-label="Client portrait"></div>
    <div class="t-name">Marin Quellet</div>
    <div class="stars">★★★★★</div>
  </div>
</section>

<!-- Call to action -->
<section class="section cta">
  <h2>Get Ready to Grow Smarter &amp; Better</h2>
  <p>Take Your Strategy to Next Level with Norvalith</p>
  <div class="btn blue" style="left:545px;top:140px;width:110px;height:39px;font-size:12px">Get Started</div>
</section>

<!-- Contact -->
<section class="section contact">
  <div class="map" role="img" aria-label="Street map of the office location and surroundings"></div>
  <h2>Contact Us</h2>
  <div class="field" style="top:115px">Name</div>
  <div class="field" style="top:168px">Company</div>
  <div class="field" style="top:221px">Email</div>
  <div class="field" style="top:275px">Phone</div>
  <div class="field" style="top:328px">Message</div>
  <div class="btn" style="left:704px;top:392px;width:97px;height:30px;font-size:12px">Submit</div>
</section>

<!-- Footer -->
<footer class="section footer">
  <div class="abs brand" style="left:121px;top:44px;font-size:34px">Norvalith</div>
  <p class="small" style="left:121px;top:95px">© 2023 Copyright Norvalith<br>All rights reserved.</p>
  <div class="divider" style="left:341px"></div>
  <div class="divider" style="left:617px"></div>
  <div class="divider" style="left:872px"></div>

  <h4 style="left:403px">Address</h4>
  <svg class="abs" style="left:403px;top:92px" width="16" height="16" viewBox="0 0 16 16"><rect width="16" height="16" fill="#e7ecf2"/><path d="M8 3 a3.5 3.5 0 0 1 3.5 3.5 C11.5 9 8 13 8 13 S4.5 9 4.5 6.5 A3.5 3.5 0 0 1 8 3Z" fill="#232b37"/></svg>
  <p class="small" style="left:427px;top:90px">418 Lakeview Plaza Suite 210,<br>Riverton, MN 55090</p>
  <svg class="abs" style="left:403px;top:132px" width="16" height="16" viewBox="0 0 16 16"><rect width="16" height="16" fill="#e7ecf2"/><path d="M5 3 L7 5 L6 7 Q7 9 9 10 L11 9 L13 11 L11.5 13 Q6 12 3 5 Z" fill="#232b37"/></svg>
  <p class="small" style="left:427px;top:133px">(555) 0143921</p>

  <h4 style="left:701px">Quick Links</h4>
  <p class="small" style="left:701px;top:82px">Home<br>About Us<br>Services<br>Insights<br>Join Us<br>Contact Us</p>

  <h4 style="left:951px">Newsletter</h4>
  <p class="small" style="left:951px;top:82px">Follow our newsletter to stay<br>updated about Norvalith</p>
  <div class="btn" style="left:951px;top:119px;width:105px;height:30px;font-size:12px">Subscribe</div>

  <div class="abs" style="left:121px;top:195px;width:430px;height:1px;background:#6b7482"></div>
  <div class="abs" style="left:649px;top:195px;width:428px;height:1px;background:#6b7482"></div>
  <div class="social" style="left:551px"></div>
  <div class="social" style="left:576px"></div>
  <div class="social" style="left:601px"></div>
  <div class="social" style="left:626px"></div>
</footer>

</body>
</html>
```